Business Card Design

After a corporate career in the finance sector I am now operating on my own as a consultant. I require a simple design, and want a strong card which is targeted at a conservative audience.

Target Market(s)

highly educated senior management, directors of companies, finance sector

Industry/Entity Type

Conservative

Contact Information for Business Card

Rosa Tindell
Consultant
Mobile: 0417 862 254
Email: rosa.tind@mailvora.com

Requirements
Should not have
• I don't want the colours green/yellow/brown

```html
<!DOCTYPE html>
<html lang="en">
<head>
<meta charset="utf-8">
<title>Rosa Tindell – Consultant</title>
<link rel="stylesheet" href="https://fonts.googleapis.com/css2?family=Gelasio:ital,wght@0,400;0,700;1,400&display=swap">
<style>
  :root {
    --paper: #ffffff;
    --ink: #0d0d0d;
    --label-blue: #1a3fc4;
    --bar-red: #e8101e;
    --bar-blue: #0a3ec8;
    --base-black: #0b0b0b;
    --serif: "Gelasio", Georgia, serif;
  }
  html, body {
    margin: 0;
    padding: 0;
    width: 1200px;
    height: 695px;
    overflow: hidden;
    background: var(--paper);
  }
  .card {
    position: relative;
    width: 1200px;
    height: 695px;
    background: var(--paper);
    font-family: var(--serif);
    color: var(--ink);
  }
  .brand {
    position: absolute;
    left: 140px;
    top: 172px;
    display: flex;
    align-items: center;
    gap: 12px;
  }
  .brand-dot {
    width: 26px;
    height: 26px;
    border-radius: 50%;
    background: var(--ink);
  }
  .brand-name {
    font-size: 36px;
    font-weight: 700;
    color: var(--ink);
    line-height: 1;
  }
  .identity {
    position: absolute;
    left: 439px;
    top: 142px;
  }
  .person-name {
    margin: 0;
    font-size: 66px;
    font-weight: 700;
    line-height: 1;
    letter-spacing: 0.3px;
  }
  .person-role {
    margin: 8px 0 0;
    font-size: 38px;
    font-style: italic;
    font-weight: 400;
    line-height: 1;
  }
  .contact {
    position: absolute;
    left: 439px;
    top: 365px;
    margin: 0;
    font-size: 38px;
    line-height: 59px;
  }
  .contact-row {
    display: flex;
  }
  .contact-label {
    color: var(--label-blue);
    width: 170px;
  }
  .contact-row.email .contact-label {
    width: 162px;
  }
  .contact-value {
    margin: 0;
    color: var(--ink);
  }
  .bar {
    position: absolute;
    top: 583px;
    height: 26px;
  }
  .bar-red {
    left: 0;
    width: 420px;
    background: var(--bar-red);
  }
  .bar-blue {
    left: 427px;
    right: 0;
    background: var(--bar-blue);
  }
  .base-band {
    position: absolute;
    left: 0;
    right: 0;
    top: 613px;
    bottom: 0;
    background: var(--base-black);
  }
</style>
</head>
<body>
  <div class="card">
    <div class="brand">
      <span class="brand-dot"></span>
      <span class="brand-name">Tindell</span>
    </div>

    <div class="identity">
      <h1 class="person-name">Rosa Tindell</h1>
      <p class="person-role">Consultant</p>
    </div>

    <dl class="contact">
      <div class="contact-row mobile">
        <dt class="contact-label">mobile</dt>
        <dd class="contact-value">0417 862 254</dd>
      </div>
      <div class="contact-row email">
        <dt class="contact-label">email</dt>
        <dd class="contact-value">rosa.tind@mailvora.com</dd>
      </div>
    </dl>

    <div class="bar bar-red"></div>
    <div class="bar bar-blue"></div>
    <div class="base-band" role="img" aria-label="Black base band with fine diagonal line texture"></div>
  </div>
</body>
</html>
```